Bamboo & Ember Business Card FUN & EXCITING

Here is the Information for the Card:
Harpreet Kalra (Toby)
E: TobyKalra@mailbox-demo.com
C: (480) 555-0147
www.BambooEmberLV.com

We don't want traditional Indian cliche, We a playful bold and fun business card.

Files: https://files.sharebox-demo.net/folders/7QtpLmzR2xVbN4kHs9wYcDfJ3eGaUoPi

https://files.sharebox-demo.net/folders/5ZrqTwyX8mKcE2vBn6aLpHsQ9uFjRgOe

Target Market(s)

Las Vegas Local Restaurant

Industry/Entity Type

Indian Restaurant

Contact Information for Business Card

Name, Email, Cell Phone, Company Logo

```html
<!DOCTYPE html>
<html lang="en">
<head>
<meta charset="utf-8">
<title>Bamboo &amp; Ember Business Card</title>
<link rel="stylesheet" href="https://fonts.googleapis.com/css2?family=Bebas+Neue&family=Open+Sans:wght@400;600&display=swap">
<style>
  :root {
    --stage: #222223;
    --teal: #0db396;
    --card-dark: #262628;
    --panel-dark: #2a2a2c;
    --yellow: #f5c518;
    --white: #ffffff;
    --text-soft: #f2f2f2;
    --food-warm: #c7782f;
    --food-deep: #6b3a1c;
    --food-light: #e7d9c4;
  }
  * { box-sizing: border-box; margin: 0; padding: 0; }
  html, body {
    width: 1200px; height: 780px; overflow: hidden;
    background: var(--stage);
  }
  .canvas {
    position: relative; width: 1200px; height: 780px;
    display: flex; justify-content: center; align-items: center; gap: 60px;
  }
  .card {
    position: relative; width: 340px; height: 590px;
    border-radius: 26px; overflow: hidden;
    box-shadow: 0 18px 40px rgba(0,0,0,0.55);
  }

  /* Front */
  .card-front { background: var(--teal); }
  .front-brand {
    position: absolute; left: 50%; top: 50%;
    transform: translate(-50%, -50%) rotate(-90deg);
    white-space: nowrap;
    font-family: "Bebas Neue", "Arial Narrow", sans-serif;
    font-size: 86px; letter-spacing: 2px; line-height: 1;
    color: var(--white);
  }

  /* Back */
  .card-back { background: var(--card-dark); }
  .back-food {
    position: absolute; left: 0; right: 0; bottom: 0; height: 250px;
    background:
      radial-gradient(circle at 78% 40%, var(--food-warm) 0 18%, transparent 30%),
      radial-gradient(circle at 30% 70%, var(--food-deep) 0 20%, transparent 34%),
      linear-gradient(135deg, var(--food-light), #b98a5a 60%, #5a3a22);
  }
  .back-panel {
    position: absolute; left: -30px; right: -30px; top: 0; height: 400px;
    background: var(--panel-dark);
    border-radius: 0 0 50% 50% / 0 0 90px 90px;
    box-shadow: 0 10px 22px rgba(0,0,0,0.5);
  }
  .back-content {
    position: relative; z-index: 1;
    display: flex; flex-direction: column; align-items: center;
    padding-top: 52px; text-align: center;
  }
  .back-brand {
    font-family: "Bebas Neue", "Arial Narrow", sans-serif;
    font-size: 50px; line-height: 1; letter-spacing: 1px;
    color: var(--white);
  }
  .person-name {
    margin-top: 42px;
    font-family: "Bebas Neue", "Arial Narrow", sans-serif;
    font-size: 32px; letter-spacing: 0.5px; line-height: 1;
    color: var(--yellow);
  }
  .contact-icons { display: flex; gap: 10px; margin-top: 12px; }
  .icon-dot {
    width: 26px; height: 26px; border-radius: 50%;
    background: var(--teal);
    display: flex; align-items: center; justify-content: center;
  }
  .icon-dot svg { width: 14px; height: 14px; }
  .contact-lines {
    margin-top: 10px;
    font-family: "Open Sans", Arial, sans-serif;
    font-size: 14px; line-height: 1.45; color: var(--text-soft);
    list-style: none;
  }
  .address-pin { margin-top: 16px; }
  .address {
    margin-top: 10px;
    font-family: "Open Sans", Arial, sans-serif;
    font-size: 13.5px; line-height: 1.45; color: var(--text-soft);
    font-style: normal;
  }
</style>
</head>
<body>
<main class="canvas">

  <section class="card card-front">
    <div class="front-brand">Bamboo &amp; Ember</div>
  </section>

  <section class="card card-back">
    <div class="back-food" role="img" aria-label="Photo of Indian dishes: grilled chicken, curry bowls and puffed bread"></div>
    <div class="back-panel"></div>
    <div class="back-content">
      <div class="back-brand">Bamboo &amp; Ember</div>
      <h1 class="person-name">Harpreet Kalra (Toby)</h1>
      <div class="contact-icons">
        <span class="icon-dot">
          <svg viewBox="0 0 24 24" fill="#fff"><path d="M6.6 10.8a15.1 15.1 0 0 0 6.6 6.6l2.2-2.2a1 1 0 0 1 1-.25 11.4 11.4 0 0 0 3.6.57 1 1 0 0 1 1 1V20a1 1 0 0 1-1 1A17 17 0 0 1 3 4a1 1 0 0 1 1-1h3.5a1 1 0 0 1 1 1c0 1.25.2 2.45.57 3.6a1 1 0 0 1-.25 1z"/></svg>
        </span>
        <span class="icon-dot">
          <svg viewBox="0 0 24 24" fill="none" stroke="#fff" stroke-width="2"><rect x="3" y="5" width="18" height="14" rx="2"/><path d="M3 7l9 6 9-6"/></svg>
        </span>
        <span class="icon-dot">
          <svg viewBox="0 0 24 24" fill="none" stroke="#fff" stroke-width="2"><circle cx="12" cy="12" r="9"/><path d="M3 12h18M12 3c3 3 3 15 0 18M12 3c-3 3-3 15 0 18"/></svg>
        </span>
      </div>
      <ul class="contact-lines">
        <li>(480) 555-0147</li>
        <li>TobyKalra@mailbox-demo.com</li>
        <li>www.BambooEmberLV.com</li>
      </ul>
      <span class="icon-dot address-pin">
        <svg viewBox="0 0 24 24" fill="none" stroke="#fff" stroke-width="2"><path d="M12 21s-6-6.2-6-11a6 6 0 0 1 12 0c0 4.8-6 11-6 11z"/><circle cx="12" cy="10" r="2.2"/></svg>
      </span>
      <address class="address">4821 Juniper Vale Rd, Suite #305,<br>Henderson, NV 89011</address>
    </div>
  </section>

</main>
</body>
</html>
```